Banner Ad and Digital Ad design for tradeshow

I need two graphics designed (can be same/similar design just different dimensions. We are an engineering firm practicing in the solid waste industry. We are a conference sponsor and need two graphics.
(1) Banner Ad - 300x250 - gif, png, jped, html, or other. Imagery with our mantra - Driven by purpose. Guided by stewardship. Striving for excellence.
(2) Digital Ad (static) - 1920x1080 hi-res jpg or png.

Target Market(s)

Solid Waste Management Industry (Environmental)

Industry/Entity Type

Environmental

Requirements
Must have
• Quality Aesthetic
Nice to have
• Great Imagery + our mantra

```html
<!DOCTYPE html>
<html lang="en">
<head>
<meta charset="utf-8">
<title>Calder Ridge Engineering – Conference Ad</title>
<link rel="stylesheet" href="https://fonts.googleapis.com/css2?family=Bebas+Neue&family=Montserrat:wght@500;700;800&display=swap">
<style>
  :root {
    --sky-top: #f09a9a;
    --sky-mid: #f6806a;
    --sky-low: #f7a45a;
    --sun: #fbd55e;
    --sun-glow: #fde9a0;
    --ground: #1e0f10;
    --ground-deep: #120909;
    --ink: #0b0b0b;
    --white: #ffffff;
    --sage: #8fa89a;
    --sage-light: #a9bdb2;
    --navy: #2a2a6a;
  }
  * { margin: 0; padding: 0; box-sizing: border-box; }
  html, body { width: 1200px; height: 974px; overflow: hidden; background: #444; }
  .ad {
    position: relative;
    width: 1200px;
    height: 974px;
    overflow: hidden;
    font-family: "Montserrat", sans-serif;
  }
  .site-scene {
    position: absolute; inset: 0;
    background:
      linear-gradient(180deg, var(--sky-top) 0%, var(--sky-mid) 35%, var(--sky-low) 52%, #d8604a 57%, var(--ground) 60%, var(--ground-deep) 100%);
  }
  .sun-section {
    position: absolute;
    left: 39px; top: 84px;
    width: 548px; height: 534px;
    border-radius: 50%;
    background: radial-gradient(circle at 50% 45%, var(--sun-glow) 0%, var(--sun) 55%, #f7b45a 100%);
  }
  .landfill-section {
    position: absolute;
    left: 11px; top: 267px;
    width: 602px; height: 216px;
    border-radius: 12px;
    background: linear-gradient(180deg, #2a1a16 0%, #120c0b 100%);
  }
  .headline {
    position: absolute;
    left: 640px; top: 92px;
    width: 500px; height: 200px;
    color: var(--ink);
    font-weight: normal;
  }
  .headline-lead {
    position: absolute;
    left: 0; top: 0;
    font-family: "Montserrat", sans-serif;
    font-weight: 800;
    font-size: 68px;
    letter-spacing: -1.5px;
    line-height: 1;
    white-space: nowrap;
  }
  .headline-main {
    position: absolute;
    left: 2px; top: 54px;
    font-family: "Bebas Neue", sans-serif;
    font-size: 166px;
    line-height: 1;
    white-space: nowrap;
  }
  .headline-cap {
    position: absolute;
    left: 402px; top: -18px;
    font-family: "Bebas Neue", sans-serif;
    font-size: 252px;
    line-height: 1;
  }
  .tagline-band {
    position: absolute;
    left: 651px; top: 296px;
    width: 478px; height: 64px;
    background: linear-gradient(90deg, rgba(11,11,11,0) 0%, var(--ink) 14%, var(--ink) 100%);
    display: flex; align-items: center; justify-content: flex-end;
    padding-right: 14px;
  }
  .tagline-band span {
    font-family: "Bebas Neue", sans-serif;
    font-size: 48px;
    letter-spacing: 1px;
    color: var(--white);
    line-height: 1;
    padding-top: 4px;
  }
  .tagline-sub {
    position: absolute;
    right: 70px; top: 380px;
    text-align: right;
    font-weight: 800;
    font-size: 32px;
    letter-spacing: 2px;
    line-height: 1.1;
    color: var(--ink);
  }
  .wave { position: absolute; inset: 0; }
  .brand-mark-large {
    position: absolute;
    left: 118px; top: 571px;
    width: 208px; height: 148px;
    display: flex; align-items: center; justify-content: center;
    font-weight: 700;
    font-size: 30px;
    color: var(--sage);
    text-align: center;
    line-height: 1.1;
  }
  .brand {
    position: absolute;
    left: 722px; top: 644px;
    display: flex; align-items: center; gap: 18px;
  }
  .brand-square { width: 76px; height: 76px; background: var(--sage); }
  .brand-name {
    font-weight: 500;
    color: var(--sage);
    font-size: 34px;
    line-height: 1.08;
    letter-spacing: 1px;
  }
  .url {
    position: absolute;
    right: 78px; top: 740px;
    font-weight: 700;
    font-size: 30px;
    color: var(--white);
  }
  .url em { font-style: normal; color: var(--sage-light); }
</style>
</head>
<body>
<main class="ad">
  <div class="site-scene" role="img" aria-label="Sunset sky over a landfill site with silhouetted haul trucks and an excavator"></div>
  <div class="sun-section" role="img" aria-label="Setting sun behind the landfill graphic"></div>
  <div class="landfill-section" role="img" aria-label="Illustration: cross-section of a capped landfill with gas wells"></div>

  <h1 class="headline">
    <span class="headline-lead">DRIVEN BY</span>
    <span class="headline-main">PURPOS</span>
    <span class="headline-cap">E</span>
  </h1>
  <div class="tagline-band"><span>GUIDED BY STEWARDSHIP</span></div>
  <p class="tagline-sub">STRIVING FOR<br>EXCELLENCE</p>

  <svg class="wave" width="1200" height="974" viewBox="0 0 1200 974" aria-hidden="true">
    <path d="M0 762 C60 735 110 726 170 728 C420 738 640 900 900 902 C1030 903 1120 820 1200 752 L1200 974 L0 974 Z" fill="var(--sage)"/>
    <path d="M90 740 C140 728 190 726 250 732 C480 760 660 905 900 906 C1000 906 1080 860 1160 790" fill="none" stroke="var(--navy)" stroke-width="4"/>
  </svg>

  <div class="brand-mark-large">CALDER<br>RIDGE</div>

  <div class="brand">
    <div class="brand-square"></div>
    <div class="brand-name">CALDER RIDGE<br>ENGINEERING</div>
  </div>
  <p class="url">www.<em>calderridgeeng</em>.com</p>
</main>
</body>
</html>
```